Indonesian B2B Company (Varo Ingredients) - Stationery Design

Varo Ingredients needs a corporate, bold and professional-looking stationery design.

Varo Ingredients is a new Indonesian company manufacturing, marketing and distributing various ingredients / raw materials such as flavours, fragrance, colours, sweeteners, preservatives for the food & beverage, pharmaceutical, personal care and other household goods industries.

It is a business to business (B2B) company as we supply various natural and synthetic raw materials to various consumer goods manufacturers. We therefore need a logo/identity with corporate and industrial style.

Varo Ingredients is a startup company which belongs to a larger Varo Tunggal group of companies (http://varotunggal.dealpathway.com/about) that focuses in the mining, petroleum and energy businesses. Varo Ingredients would like to focus in providing good quality, safe, reliable and affordable ingredients for the industries. Our tagline is "Quality Inputs, Trusted Supply"
Updates

We have updated some information including our requirements and contact details to be shown in the stationery. Please check the project brief.

Regards,

Varo Ingredients

Target Market(s)

Manufacturers of food & beverages, personal care, pharmaceutical and other FMCG factories.

Industry/Entity Type

Business

Requirements
Must have
• Smart, professional and corporate touches in the stationery designs. We require designs for:
1. Letterhead
2. Envelope (with and without window)
3. Name card
4. Powerpoint presentation template
5. CD label
6. Small memo / with compliments card

Contact details:

Company name:
PT Varo Ingredients

Address:
Ruko Melati Sentosa Utara, Blok K07 no: 15-16
Duren Sawit Selatan, 13470
Indonesia

Tel:+62 21 738 2906
Fax:+62 21 738 2907
Email: info@varo-ingredients.co.id
Website: www.varo-ingredients.co.id

```html
<!DOCTYPE html>
<html lang="en">
<head>
<meta charset="utf-8">
<title>Varo Ingredients – Stationery Set</title>
<link href="https://fonts.googleapis.com/css2?family=Barlow:wght@400;500;600;700&display=swap" rel="stylesheet">
<style>
  :root {
    --red: #c8102e;
    --red-dark: #a50d26;
    --orange: #f5a623;
    --ink: #3a3a3a;
    --grey: #777777;
    --paper: #ffffff;
    --backdrop: #e6e4e0;
    --fold: #dcdcdc;
  }
  * { margin: 0; padding: 0; box-sizing: border-box; }
  html, body { width: 1200px; height: 900px; overflow: hidden; }
  body { background: var(--backdrop); font-family: "Barlow", sans-serif; color: var(--ink); position: relative; }
  address { font-style: normal; }

  .sheet { position: absolute; background: var(--paper); box-shadow: 0 2px 8px rgba(0,0,0,.18); overflow: hidden; }

  /* Footer bands: thin orange rule over a solid red bar */
  .footer-band { position: absolute; left: 0; right: 0; bottom: 0; background: var(--red); }
  .footer-band::before { content: ""; position: absolute; left: 0; right: 0; top: -8px; height: 4px; background: var(--orange); }

  .brand { display: flex; align-items: center; gap: 8px; white-space: nowrap; }
  .brand-mark { background: var(--red); flex: none; }
  .brand-name { color: var(--red); font-weight: 700; line-height: 1; }
  .tagline { color: var(--grey); font-weight: 400; white-space: nowrap; }

  /* Letterhead */
  .letterhead { left: 50px; top: 102px; width: 498px; height: 705px; }
  .letterhead .brand { position: absolute; left: 30px; top: 32px; }
  .letterhead .brand-mark { width: 22px; height: 22px; }
  .letterhead .brand-name { font-size: 20px; }
  .letterhead .tagline { position: absolute; left: 30px; top: 62px; font-size: 9.5px; }
  .contact-block { position: absolute; right: 28px; top: 20px; width: 150px; text-align: right; font-size: 8.5px; line-height: 1.4; border-left: 1px solid #ddd; }
  .contact-block .company { color: var(--red); font-size: 10px; font-weight: 600; margin-bottom: 12px; }
  .contact-block .gap { height: 8px; }
  .letterhead .footer-band { height: 70px; }
  .site-line { position: absolute; right: 30px; bottom: 14px; color: #fff; font-size: 11px; letter-spacing: 2px; }

  /* Business cards */
  .card { width: 213px; height: 117px; top: 123px; }
  .card-front { left: 657px; }
  .card-back { left: 885px; background: var(--red); }
  .card-front .brand { position: absolute; left: 14px; top: 16px; gap: 5px; }
  .card-front .brand-mark { width: 10px; height: 10px; }
  .card-front .brand-name { font-size: 10px; }
  .card-front .tagline { position: absolute; left: 14px; top: 30px; font-size: 5.5px; }
  .card-details { position: absolute; left: 118px; top: 12px; font-size: 5.5px; line-height: 1.3; }
  .card-details .person { color: var(--red); font-size: 8px; font-weight: 600; }
  .card-details .role { margin-bottom: 4px; }
  .card-details .company { color: var(--red); font-weight: 600; }
  .card-front .footer-band { height: 16px; }
  .card-front .footer-band::before { top: -5px; height: 2px; }
  .card-back .brand { position: absolute; left: 50%; top: 40px; transform: translateX(-50%); }
  .card-back .brand-mark { width: 12px; height: 12px; background: #fff; }
  .card-back .brand-name { color: #fff; font-size: 13px; }
  .card-back .footer-band { height: 18px; background: var(--red-dark); }
  .card-back .footer-band::before { top: -5px; height: 2px; }
  .card-back .card-site { position: absolute; left: 30px; bottom: 5px; color: #fff; font-size: 6px; letter-spacing: 1px; }

  /* Window envelope */
  .envelope-front { left: 585px; top: 275px; width: 570px; height: 243px; }
  .envelope-front .brand { position: absolute; left: 28px; top: 40px; }
  .envelope-front .brand-mark { width: 20px; height: 20px; }
  .envelope-front .brand-name { font-size: 17px; }
  .envelope-front .tagline { position: absolute; left: 28px; top: 66px; font-size: 8px; }
  .address-window { position: absolute; left: 20px; top: 122px; width: 198px; height: 72px; border: 1px solid #e0509a; border-radius: 2px; }
  .envelope-front .footer-band { height: 34px; }
  .envelope-front .footer-band::before { top: -9px; height: 4px; }

  /* Envelope back */
  .envelope-back { left: 585px; top: 540px; width: 570px; height: 246px; }
  .flap { position: absolute; inset: 0; width: 100%; height: 100%; }
  .envelope-back .brand { position: absolute; left: 50%; top: 30px; transform: translateX(-50%); }
  .envelope-back .brand-mark { width: 16px; height: 16px; }
  .envelope-back .brand-name { font-size: 15px; }
  .return-address { position: absolute; left: 0; right: 0; top: 200px; text-align: center; font-size: 7.5px; line-height: 1.4; }
  .return-address .company { color: var(--red); font-weight: 600; font-size: 8.5px; }
</style>
</head>
<body>

<section class="sheet letterhead" aria-label="Letterhead">
  <div class="brand"><span class="brand-mark"></span><span class="brand-name">Varo Ingredients</span></div>
  <p class="tagline">Quality Inputs, Trusted Supply</p>
  <address class="contact-block">
    <p class="company">PT Varo Ingredients</p>
    <p>Ruko Melati Sentosa Utara,<br>Blok K07 no: 15-16<br>Duren Sawit Selatan, 13470<br>Indonesia</p>
    <div class="gap"></div>
    <p>Tel:+62 21 738 2906<br>Fax:+62 21 738 2907<br>Email: info@varo-ingredients.co.id</p>
  </address>
  <div class="footer-band"></div>
  <p class="site-line">www.varo-ingredients.co.id</p>
</section>

<section class="sheet card card-front" aria-label="Business card, front">
  <div class="brand"><span class="brand-mark"></span><span class="brand-name">Varo Ingredients</span></div>
  <p class="tagline">Quality Inputs, Trusted Supply</p>
  <address class="card-details">
    <p class="person">Dimas Arfianto</p>
    <p class="role">General Manager</p>
    <p class="company">PT Varo Ingredients</p>
    <p>Ruko Melati Sentosa Utara<br>Blok K07 no: 15-16<br>Duren Sawit Selatan, 13470</p>
    <p>+62 21 738 2906<br>info@varo-ingredients.co.id</p>
  </address>
  <div class="footer-band"></div>
</section>

<section class="sheet card card-back" aria-label="Business card, back">
  <div class="brand"><span class="brand-mark"></span><span class="brand-name">Varo Ingredients</span></div>
  <div class="footer-band"></div>
  <p class="card-site">www.varo-ingredients.co.id</p>
</section>

<section class="sheet envelope-front" aria-label="Window envelope">
  <div class="brand"><span class="brand-mark"></span><span class="brand-name">Varo Ingredients</span></div>
  <p class="tagline">Quality Inputs, Trusted Supply</p>
  <div class="address-window"></div>
  <div class="footer-band"></div>
</section>

<section class="sheet envelope-back" aria-label="Envelope, back">
  <svg class="flap" viewBox="0 0 570 246" preserveAspectRatio="none">
    <path d="M0 0 L285 110 L570 0" fill="none" stroke="var(--fold)" stroke-width="1"/>
    <path d="M0 246 L170 90 M570 246 L400 90" fill="none" stroke="var(--fold)" stroke-width="1"/>
  </svg>
  <div class="brand"><span class="brand-mark"></span><span class="brand-name">Varo Ingredients</span></div>
  <address class="return-address">
    <p class="company">PT Varo Ingredients</p>
    <p>Ruko Melati Sentosa Utara, Blok K07 no: 15-16 Duren Sawit Selatan, 13470 Indonesia</p>
    <p>Tel:+62 21 738 2906 &nbsp;Fax:+62 21 738 2907 &nbsp;Email: info@varo-ingredients.co.id</p>
  </address>
</section>

</body>
</html>
```